Business Card Design Project

We need a business card designed for a new Luxury Custom Homebuilding company based in Arizona. We previous were called "Brellcrest Estates" but want to start using "Brellcrest Custom Homes" We want the message to communicate high end, luxury and cutting-edge. We like the blue, white and black color scheme.
Brellcrest Custom Homes
Marcus T. Pellingham
Chief Executive Officer
Office: 480-555-0142
Mobile: 480-555-0173
email: marcus@brellcrestcustom.com
web adress: www.BrellcrestCustom.com
Updates
We have made a change to our website address and email address based on recieving feedback from a nmber of individuals. The feedback was web address and email address was to long. Therefore we have made a change. The new web adress and email adress are the following.
www.BrellcrestCustom.com
marcus@brellcrestcustom.com
Also I decided against using in yellow. I like the colors blue,black, white and maybe gray.
Target Market(s)
Our target market is the wealthy individuals looking for a luxury high-end custom home.
Industry/Entity Type
Business
Look and feel
Each slider illustrates characteristics of the customer's brand and the style your logo design should communicate.

```html
<!DOCTYPE html>
<html lang="en">
<head>
<meta charset="utf-8">
<title>Brellcrest Custom Homes – Business Card</title>
<link rel="stylesheet" href="https://fonts.googleapis.com/css2?family=Jost:wght@300;400;600&family=PT+Sans:wght@400&display=swap">
<style>
  :root {
    --page-bg: #1c1d1f;
    --band: #0e1216;
    --steel-light: #6a8db0;
    --steel-dark: #36536f;
    --slate-light: #45484c;
    --slate-dark: #1f2124;
    --ink-white: #f2f4f6;
    --ink-grey: #b9bec4;
    --accent-blue: #5f8fc4;
  }
  * { margin: 0; padding: 0; box-sizing: border-box; }
  html, body { width: 1200px; height: 900px; overflow: hidden; }
  body {
    background: var(--page-bg);
    display: flex;
    flex-direction: column;
    align-items: center;
    justify-content: center;
    gap: 24px;
    font-family: "PT Sans", sans-serif;
  }
  .card {
    position: relative;
    width: 700px;
    height: 400px;
    border-radius: 18px;
    overflow: hidden;
    background: linear-gradient(135deg, var(--slate-light), var(--slate-dark));
    box-shadow: 0 10px 30px rgba(0,0,0,.5);
  }
  .card__texture-blue {
    position: absolute;
    top: 0; bottom: 0; left: 0;
    width: 290px;
    background: radial-gradient(ellipse at 40% 40%, var(--steel-light), var(--steel-dark) 85%);
  }
  .card--back .card__texture-blue { width: 330px; }
  .card__band {
    position: absolute;
    left: 0; right: 0;
    height: 22px;
    background: var(--band);
    opacity: .85;
  }
  .card__band--top { top: 0; }
  .card__band--bottom { bottom: 0; }

  .holder { position: absolute; left: 30px; top: 56px; }
  .holder__name {
    font-family: "Jost", sans-serif;
    font-weight: 300;
    font-size: 31px;
    color: var(--ink-white);
    letter-spacing: .5px;
  }
  .holder__title {
    font-family: "Jost", sans-serif;
    font-weight: 400;
    font-size: 13px;
    color: var(--ink-grey);
    margin-top: 2px;
    margin-left: 4px;
  }

  .brand-name {
    position: absolute;
    font-family: "Jost", sans-serif;
    font-weight: 600;
    color: var(--ink-white);
    line-height: 1;
    text-transform: none;
  }
  .card--front .brand-name { left: 240px; top: 118px; font-size: 52px; }
  .card--back .brand-name { left: 190px; top: 150px; font-size: 52px; }

  .contact {
    position: absolute;
    left: 32px;
    bottom: 42px;
    font-size: 15px;
    line-height: 1.45;
    color: var(--ink-white);
  }
  .label { color: var(--accent-blue); }

  .web-line {
    position: absolute;
    font-size: 14px;
    color: var(--ink-grey);
  }
  .card--front .web-line { right: 34px; bottom: 44px; }
  .card--back .web-line { right: 34px; top: 40px; font-size: 13px; }
</style>
</head>
<body>

  <section class="card card--front" aria-label="Business card front">
    <div class="card__texture-blue" role="img" aria-label="Blue grunge texture panel"></div>
    <div class="card__band card__band--top"></div>
    <div class="card__band card__band--bottom"></div>

    <div class="holder">
      <p class="holder__name">Marcus T. Pellingham</p>
      <p class="holder__title">Chief Executive Officer</p>
    </div>

    <p class="brand-name">Brellcrest<br>Custom Homes</p>

    <p class="web-line"><span class="label">Website:</span> www.BrellcrestCustom.com</p>

    <div class="contact">
      <p><span class="label">Office:</span> 480-555-0142</p>
      <p><span class="label">Mobile:</span> 480-555-0173</p>
      <p><span class="label">Email:</span> marcus@brellcrestcustom.com</p>
    </div>
  </section>

  <section class="card card--back" aria-label="Business card back">
    <div class="card__texture-blue" role="img" aria-label="Blue grunge texture panel"></div>
    <div class="card__band card__band--top"></div>
    <div class="card__band card__band--bottom"></div>

    <p class="brand-name">Brellcrest<br>Custom Homes</p>

    <p class="web-line">www.BrellcrestCustom.com</p>
  </section>

</body>
</html>
```